ボトル容器(280mL入り・画像参照)のオモテ面のラベルデザインを依頼します。
「食器洗いを楽しく!」というコンセプトを、手肌と環境へのやさしさという要素を盛り込みながら、ラベルのデザインとして表現してください。
パラダイスを感じさせるような、明るく、楽しく、元気でウキウキ、ワクワクするような雰囲気と同時に、予定価格が280mL入で1,300円前後と通常の食器洗剤と比べて高価格帯なので、安っぽさを感じさせない高級感も考慮してください。
当商品は今後、香りのバリエーション展開を予定しているので、ラベルの一部の色を替えることで、複数の香りバリエーションに対応できるデザインを希望します。
ラベルサイズ:幅50mm×高さ75mm以上100mm以下

以下の要素を入れてください。
商品名:Fluvorne
商品名の読み:フルヴォーン
品名:台所用せっけん
香り:○○○の香り
メインキャッチコピー:食器洗いを楽しく!
サブキャッチコピー:手肌と環境を守る水せっけん
シンプル 複雑
単色 カラフル
暗い 明るい
日常 高級
遊び心 厳粛
未来的 伝統的
女性的 男性的
• 高解像度JPG (.jpg)
• イラストレーター形式 (.ai)
添付画像のボトルに貼られたラベルのサイズは幅50mm×高さ75mmです。

コンセプトを最もよく表現していただいた提案でした。

とてもレベルの高い提案ばかりで、たいへん感謝しております。ありがとうございました。

```html
<!DOCTYPE html>
<html lang="ja">
<head>
<meta charset="UTF-8">
<title>Fluvorne ラベル</title>
<link href="https://fonts.googleapis.com/css2?family=Marcellus&family=Noto+Serif+JP:wght@500;600&display=swap" rel="stylesheet">
<style>
  :root {
    --page: #ffffff;
    --label-green: #4fae84;
    --leaf-light: #b5d98f;
    --leaf-mid: #7cc48e;
    --leaf-deep: #2f8f62;
    --ink-dark: #1d4a2f;
    --ink-light: #ffffff;
    --caption: #333333;
  }
  html, body {
    margin: 0;
    padding: 0;
    width: 744px;
    height: 1200px;
    overflow: hidden;
    background: var(--page);
  }
  .canvas {
    position: relative;
    width: 744px;
    height: 1200px;
  }
  .label {
    position: absolute;
    left: 105px;
    top: 40px;
    width: 534px;
    height: 908px;
    background: var(--label-green);
    overflow: hidden;
    text-align: center;
  }
  .pattern {
    position: absolute;
    left: 0;
    width: 100%;
  }
  .pattern--top {
    top: 0;
    height: 230px;
    background: linear-gradient(180deg, var(--leaf-deep) 0%, var(--leaf-mid) 45%, var(--leaf-light) 75%, var(--label-green) 100%);
  }
  .pattern--bottom {
    bottom: 0;
    height: 215px;
    background: linear-gradient(0deg, var(--leaf-deep) 0%, var(--leaf-mid) 45%, var(--leaf-light) 75%, var(--label-green) 100%);
  }
  .catch {
    position: absolute;
    left: 0;
    width: 100%;
    margin: 0;
    font-family: "Noto Serif JP", serif;
    font-weight: 600;
    color: var(--ink-dark);
    font-size: 36px;
    letter-spacing: 2px;
    top: 300px;
  }
  .reading {
    position: absolute;
    left: 0;
    width: 100%;
    top: 372px;
    font-family: "Noto Serif JP", serif;
    font-weight: 500;
    font-size: 22px;
    letter-spacing: 3px;
    color: var(--ink-light);
  }
  .product-name {
    position: absolute;
    left: 0;
    width: 100%;
    top: 388px;
    margin: 0;
    font-family: "Marcellus", serif;
    font-weight: 400;
    font-size: 100px;
    line-height: 1.1;
    color: var(--ink-light);
  }
  .sub-catch {
    position: absolute;
    left: 0;
    width: 100%;
    top: 505px;
    margin: 0;
    font-family: "Noto Serif JP", serif;
    font-weight: 600;
    font-size: 29px;
    line-height: 1.45;
    letter-spacing: 1px;
    color: var(--ink-dark);
  }
  .scent {
    position: absolute;
    left: 0;
    width: 100%;
    top: 625px;
    margin: 0;
    font-family: "Noto Serif JP", serif;
    font-weight: 500;
    font-size: 34px;
    letter-spacing: 2px;
    color: var(--ink-light);
  }
  .size-note {
    position: absolute;
    right: 110px;
    top: 1118px;
    font-family: "Noto Serif JP", serif;
    font-size: 22px;
    color: var(--caption);
  }
</style>
</head>
<body>
  <div class="canvas">
    <div class="label">
      <div class="pattern pattern--top" role="img" aria-label="緑と黄緑の葉が並ぶ装飾パターン"></div>
      <div class="pattern pattern--bottom" role="img" aria-label="緑と黄緑の葉が並ぶ装飾パターン"></div>
      <p class="catch">食器洗いを楽しく!</p>
      <div class="reading">フルヴォーン</div>
      <h1 class="product-name">Fluvorne</h1>
      <p class="sub-catch">手肌と環境を守る<br>台所用 水せっけん</p>
      <p class="scent">ミントの香り</p>
    </div>
    <div class="size-note">50×85mm</div>
  </div>
</body>
</html>
```